Korvanta Corporate Vision Mission Statement Infographic

We need an info graphic which summarizes and visually explains the companies Ambition Statement, Strategic Priorities, Principles and Brand Actions and how they relate to each other

Need extra days to review

```html
<!DOCTYPE html>
<html lang="en">
<head>
<meta charset="utf-8">
<title>Korvanta – Ambition, Priorities, Principles</title>
<link href="https://fonts.googleapis.com/css2?family=Lato:wght@300;400;700;900&display=swap" rel="stylesheet">
<style>
  :root {
    --orange: #f26b2f;
    --blue: #2f5aa8;
    --blue-mid: #3f6fc0;
    --blue-light: #8fb0de;
    --blue-pale: #c9d8ef;
    --ink: #3a3a3a;
    --grey-line: #c8c8c8;
    --card-bg: #eef1f7;
    --white: #ffffff;
  }
  * { box-sizing: border-box; margin: 0; padding: 0; }
  html, body { width: 855px; height: 1200px; overflow: hidden; background: var(--white); }
  body { font-family: "Lato", Arial, sans-serif; color: var(--ink); }
  .canvas { position: relative; width: 855px; height: 1200px; overflow: hidden; }

  .brand { position: absolute; left: 48px; top: 44px; font-size: 36px; font-weight: 700; color: var(--blue); line-height: 1; }

  .tagline { position: absolute; right: 45px; top: 44px; font-size: 38px; font-weight: 400; letter-spacing: -0.3px; }
  .tagline .t-blue { color: var(--blue-mid); }
  .tagline .t-dark { color: var(--ink); }
  .tagline .t-orange { color: var(--orange); }
  .header-rule { position: absolute; left: 45px; top: 117px; width: 600px; height: 3px; background: var(--grey-line); }

  .deco-corner { position: absolute; right: 0; top: 0; width: 130px; height: 250px;
    background: linear-gradient(160deg, rgba(143,176,222,0.35), rgba(143,176,222,0.05)); border-bottom-left-radius: 60px; }

  .hero-photo { position: absolute; left: 57px; top: 145px; width: 368px; height: 302px; border-radius: 22px;
    background: linear-gradient(180deg, #f6b46a 0%, #e98a3e 35%, #8a8a55 65%, #5d6b3d 100%); }

  .ambition { position: absolute; left: 466px; top: 225px; width: 320px; }
  .ambition h2 { font-size: 33px; font-weight: 700; color: var(--orange); letter-spacing: 0.5px; line-height: 1.1; }
  .ambition .rule { height: 2px; background: var(--grey-line); margin: 4px 0 10px; width: 300px; }
  .ambition p { font-size: 16px; line-height: 22px; font-weight: 700; color: var(--blue); width: 310px; hyphens: auto; }

  .priorities { position: absolute; left: 0; top: 483px; width: 855px; height: 282px; background: var(--orange); color: var(--white); }
  .priorities h2 { text-align: center; font-size: 28px; font-weight: 700; letter-spacing: 1.5px; margin-top: 14px; }
  .priorities .rule { width: 360px; height: 2px; background: var(--white); margin: 6px auto 0; }
  .priority { position: absolute; top: 88px; width: 240px; text-align: center; }
  .priority-icon { width: 96px; height: 96px; margin: 0 auto; border-radius: 50%; background: rgba(255,255,255,0.22); }
  .priority span { display: block; margin-top: 18px; font-size: 14px; font-weight: 700; letter-spacing: 0.4px; line-height: 19px; text-transform: uppercase; }
  .divider { position: absolute; top: 87px; width: 3px; height: 142px; background: var(--white); }

  .principles-title { position: absolute; top: 782px; left: 0; width: 855px; text-align: center; font-size: 26px; font-weight: 700; color: var(--blue); letter-spacing: 0.6px; }
  .principles-rule { position: absolute; top: 820px; left: 225px; width: 405px; height: 2px; background: var(--grey-line); }

  .timeline { position: absolute; top: 830px; left: 0; }

  .cards { position: absolute; top: 982px; left: 45px; width: 765px; display: flex; gap: 11px; }
  .card { position: relative; width: 144px; height: 180px; }
  .card-head { position: absolute; top: 18px; left: 0; width: 100%; height: 28px; background: var(--blue); }
  .card-head::before { content: ""; position: absolute; left: 50%; top: -18px; margin-left: -16px;
    border-left: 16px solid transparent; border-right: 16px solid transparent; border-bottom: 18px solid var(--blue); }
  .card-body { position: absolute; top: 46px; left: 0; width: 100%; height: 134px; background: var(--card-bg); text-align: center; padding-top: 12px; }
  .label-principle { font-size: 15px; font-weight: 900; color: var(--orange); }
  .value-principle { font-size: 18px; font-weight: 300; color: var(--ink); text-transform: uppercase; margin-top: 1px; }
  .card-rule { width: 112px; height: 2px; background: var(--blue); margin: 4px auto 5px; }
  .label-action { font-size: 15px; font-weight: 900; color: var(--blue); }
  .value-action { font-size: 13px; color: var(--ink); margin-top: 2px; }
</style>
</head>
<body>
<div class="canvas">

  <div class="deco-corner" role="img" aria-label="Faint travel-themed corner decoration"></div>

  <div class="brand">Korvanta</div>

  <div class="tagline"><span class="t-blue">Dream.</span> <span class="t-dark">Explore.</span> <span class="t-orange">Travel On.</span></div>
  <div class="header-rule"></div>

  <div class="hero-photo" role="img" aria-label="Photo of a traveller with a backpack raising both arms on a hilltop at sunset"></div>

  <section class="ambition">
    <h2>AMBITION</h2>
    <div class="rule"></div>
    <p>Our dream is to be a globally recognized travel protection provider with heart—strive to be the best in the eyes of our customers as they travel and explore the world safely.</p>
  </section>

  <section class="priorities">
    <h2>STRATEGIC PRIORITIES</h2>
    <div class="rule"></div>

    <div class="priority" style="left:30px;">
      <div class="priority-icon" role="img" aria-label="Icon for customer experience"></div>
      <span>Transform the<br>customer experience</span>
    </div>
    <div class="divider" style="left:303px;"></div>

    <div class="priority" style="left:307px;">
      <div class="priority-icon" role="img" aria-label="Icon for simplicity"></div>
      <span>Simplify<br>the complex</span>
    </div>
    <div class="divider" style="left:567px;"></div>

    <div class="priority" style="left:585px;">
      <div class="priority-icon" role="img" aria-label="Icon for partnerships"></div>
      <span>Build successful<br>partnerships</span>
    </div>
  </section>

  <h2 class="principles-title">PRINCIPLES AND BRAND ACTIONS</h2>
  <div class="principles-rule"></div>

  <svg class="timeline" width="855" height="140" viewBox="0 0 855 140">
    <rect x="45" y="46" width="765" height="36" rx="18" fill="#3f6fc0"/>
    <g fill="#fff" stroke="#c9d8ef" stroke-width="5">
      <circle cx="112" cy="64" r="40"/>
      <circle cx="277" cy="64" r="40"/>
      <circle cx="435" cy="64" r="40"/>
      <circle cx="592" cy="64" r="40"/>
      <circle cx="750" cy="64" r="40"/>
    </g>
    <g fill="#dbe5f4">
      <circle cx="112" cy="64" r="22" role="img" aria-label="Icon for excellence"/>
      <circle cx="277" cy="64" r="22" role="img" aria-label="Icon for commitment"/>
      <circle cx="435" cy="64" r="22" role="img" aria-label="Icon for compassion"/>
      <circle cx="592" cy="64" r="22" role="img" aria-label="Icon for integrity"/>
      <circle cx="750" cy="64" r="22" role="img" aria-label="Icon for independence"/>
    </g>
  </svg>

  <div class="cards">
    <div class="card"><div class="card-head"></div><div class="card-body">
      <div class="label-principle">PRINCIPLE:</div><div class="value-principle">Excellence</div><div class="card-rule"></div>
      <div class="label-action">BRAND ACTION:</div><div class="value-action">Embrace challenge</div></div></div>
    <div class="card"><div class="card-head"></div><div class="card-body">
      <div class="label-principle">PRINCIPLE:</div><div class="value-principle">Commitment</div><div class="card-rule"></div>
      <div class="label-action">BRAND ACTION:</div><div class="value-action">Go the extra mile</div></div></div>
    <div class="card"><div class="card-head"></div><div class="card-body">
      <div class="label-principle">PRINCIPLE:</div><div class="value-principle">Compassion</div><div class="card-rule"></div>
      <div class="label-action">BRAND ACTION:</div><div class="value-action">Put people first</div></div></div>
    <div class="card"><div class="card-head"></div><div class="card-body">
      <div class="label-principle">PRINCIPLE:</div><div class="value-principle">Integrity</div><div class="card-rule"></div>
      <div class="label-action">BRAND ACTION:</div><div class="value-action">Do the right thing</div></div></div>
    <div class="card"><div class="card-head"></div><div class="card-body">
      <div class="label-principle">PRINCIPLE:</div><div class="value-principle">Independence</div><div class="card-rule"></div>
      <div class="label-action">BRAND ACTION:</div><div class="value-action">Be extraordinary</div></div></div>
  </div>

</div>
</body>
</html>
```